2018 Mother's Day and Baby Blessing poster

I need a poster Mother's Day and Baby Blessing ceremony for a Jade Petal Celebration at Sydney Kestrel Cove. There is no specification on the design, however the only requirement is to present mother and baby in the poster. I would like the design to be modern, attractive and simple.

Must have:
Date: 13/5/2018 (Sunday)
Time: 2:00pm (1:00pm registration)
Venue: Wirraminta Park, Kestrel Cove
Logo

```html
<!DOCTYPE html>
<html lang="en">
<head>
<meta charset="utf-8">
<title>Mother's Day &amp; Baby Blessing 2018</title>
<link rel="stylesheet" href="https://fonts.googleapis.com/css2?family=Montserrat:wght@500;600;700;800&family=Lora:wght@500&display=swap">
<style>
  :root {
    --paper: #ffffff;
    --photo-dark: #dc8ea7;
    --photo-mid: #eeb4c6;
    --photo-light: #f8dbe4;
    --bloom: #eea1b8;
    --magenta: #c8235f;
    --plum: #3b1d47;
  }
  * { margin: 0; padding: 0; box-sizing: border-box; }
  html, body { width: 849px; height: 1200px; overflow: hidden; background: var(--paper); }
  .poster {
    position: relative;
    width: 849px;
    height: 1200px;
    overflow: hidden;
    background: var(--paper);
    font-family: "Montserrat", sans-serif;
    color: var(--plum);
  }
  .hero-photo {
    position: absolute;
    left: 0; top: 0;
    width: 849px; height: 600px;
    background:
      radial-gradient(ellipse 210px 230px at 560px 260px, var(--photo-light) 0%, rgba(248,219,228,0) 100%),
      linear-gradient(120deg, var(--photo-dark) 0%, var(--photo-mid) 45%, #f3c4d2 100%);
    -webkit-mask-image: linear-gradient(180deg, #000 70%, transparent 100%);
    mask-image: linear-gradient(180deg, #000 70%, transparent 100%);
  }
  .bloom {
    position: absolute;
    left: 60px; top: 420px;
    width: 730px; height: 620px;
    border-radius: 50%;
    background: radial-gradient(ellipse at 50% 50%, var(--bloom) 0%, #f3b9ca 38%, rgba(246,206,218,0.7) 58%, rgba(255,255,255,0) 72%);
  }
  .headline {
    position: absolute;
    left: 0; right: 0; top: 500px;
    text-align: center;
  }
  .year {
    font-weight: 600;
    font-size: 38px;
    line-height: 1;
  }
  .title {
    font-weight: 700;
    font-size: 56px;
    line-height: 1.1;
    text-transform: uppercase;
    margin-top: 14px;
  }
  .title .amp { font-size: 40px; }
  .day {
    font-weight: 600;
    font-size: 64px;
    color: var(--magenta);
    line-height: 1;
    margin-top: 12px;
  }
  .date {
    font-weight: 500;
    font-size: 44px;
    line-height: 1;
    margin-top: 6px;
  }
  .time {
    font-family: "Lora", serif;
    font-weight: 500;
    font-size: 21px;
    margin-top: 12px;
  }
  .venue {
    position: absolute;
    left: 0; right: 0; top: 895px;
    text-align: center;
    font-size: 33px;
    font-weight: 700;
  }
  .organiser {
    position: absolute;
    left: 0; right: 0; top: 1040px;
    display: flex;
    justify-content: center;
    align-items: center;
    gap: 18px;
  }
  .organiser-mark { width: 30px; height: 30px; background: var(--plum); }
  .organiser-name { font-weight: 700; font-size: 40px; color: var(--plum); }
</style>
</head>
<body>
  <main class="poster">
    <div class="hero-photo" role="img" aria-label="Soft pink photograph of a mother kissing the cheek of her smiling baby"></div>
    <div class="bloom" role="img" aria-label="Pink powder burst behind the event details"></div>

    <header class="headline">
      <p class="year">2018</p>
      <h1 class="title">Mother's Day <span class="amp">&amp;</span><br>Baby Blessing</h1>
      <p class="day">SUNDAY</p>
      <p class="date">13 MAY 2018</p>
      <p class="time">2:00pm (1:00pm registration)</p>
    </header>

    <p class="venue">Wirraminta Park, Kestrel Cove</p>

    <footer class="organiser">
      <span class="organiser-mark"></span>
      <span class="organiser-name">Jade Petal Celebration</span>
    </footer>
  </main>
</body>
</html>
```